Yacht Management in Miami & Ft Lauderdale (2019Q2)

I’m looking for a flyer to leave places for people to get information about my company and what services we offer.
We offer monthly management plans to ensure the vessel is ready to go at a moments notice. This can be as simple as washing once a week, or as involved as washing, waxing, detailing, provisioning, and crew services.
We also offer bespoke customizations; stereos, on board WiFi, and engineering.

Target Market(s)

Yacht and boat owners.

Font styles to use
Sans Serif

Colors
87d0c7
85cae6
85acd3
cedeed
cee9f5
cfeae6
0455a3

Requirements
Must have
• Must have simple attention grabbing, without being obnoxious.
• Prefer a 3in x 5in post card size. other size may be an option.
• Must be front and back.
Nice to have
• Languages: English, Spanish, Russian
• USA flag logo
Should not have
• Should not have a lot of text. Icons and photos are great.

```html
<!DOCTYPE html>
<html lang="en">
<head>
<meta charset="utf-8">
<title>Harbor Keep – Postcard Front and Back</title>
<link href="https://fonts.googleapis.com/css2?family=Montserrat:wght@200;300;400;500;600;700;800&display=swap" rel="stylesheet">
<style>
  :root {
    --page-bg: #e4e0dc;
    --sea-deep: #0c4a52;
    --sea-mid: #136069;
    --sea-light: #2b7a80;
    --brand-red: #c41a33;
    --ink-black: #111111;
    --white: #ffffff;
  }
  * { box-sizing: border-box; margin: 0; padding: 0; }
  html, body {
    width: 1200px; height: 1200px; overflow: hidden;
    background: var(--page-bg);
    font-family: "Montserrat", Arial, sans-serif;
  }
  .canvas { position: relative; width: 1200px; height: 1200px; }
  .card {
    position: absolute; top: 238px; width: 444px; height: 664px;
    overflow: hidden; color: var(--white);
    box-shadow: 0 2px 6px rgba(0,0,0,0.18);
  }
  /* Front */
  .card--front { left: 136px; }
  .sea-photo {
    position: absolute; inset: 0 0 11px 0;
    background: radial-gradient(ellipse at 50% 30%, var(--sea-light) 0%, var(--sea-mid) 45%, var(--sea-deep) 100%);
  }
  .front-title {
    position: absolute; left: 0; right: 0; top: 314px;
    text-align: center; line-height: 0.86; letter-spacing: -1px;
  }
  .front-title .thin { display: block; font-weight: 200; font-size: 64px; }
  .front-title .bold { display: block; font-weight: 700; font-size: 80px; }
  .front-title .bold--wide { font-size: 82px; }
  .brand-name {
    font-weight: 700; text-transform: uppercase; text-align: center;
    line-height: 1; letter-spacing: 1px;
  }
  .front-brand {
    position: absolute; left: 0; right: 0; top: 524px; font-size: 15px;
  }
  .front-brand .dot {
    display: block; width: 10px; height: 10px; border-radius: 50%;
    background: var(--white); margin: 0 auto 7px;
  }
  .stripe { position: absolute; bottom: 0; height: 11px; width: 50%; }
  .stripe--black { left: 0; background: var(--ink-black); }
  .stripe--red { right: 0; background: var(--brand-red); }

  /* Back */
  .card--back { left: 642px; background: var(--brand-red); }
  .helm-icon { position: absolute; left: 190px; top: 44px; width: 64px; height: 64px; }
  .back-kicker {
    position: absolute; left: 0; right: 0; top: 116px;
    text-align: center; font-weight: 300; font-size: 23px; letter-spacing: 0.5px;
  }
  .back-title {
    position: absolute; left: 0; right: 0; top: 140px;
    text-align: center; font-weight: 700; font-size: 39px; letter-spacing: -0.5px;
  }
  .title-rule {
    position: absolute; left: 158px; width: 128px; top: 190px; height: 1px;
    background: rgba(255,255,255,0.6);
  }
  .back-intro {
    position: absolute; left: 50px; right: 50px; top: 206px;
    text-align: center; font-size: 12.3px; line-height: 1.25;
  }
  .feature { position: absolute; left: 68px; right: 40px; }
  .feature__icon { position: absolute; left: 0; width: 34px; height: 34px; }
  .feature__body { position: absolute; left: 45px; right: 0; top: 0; }
  .feature__name { font-weight: 600; font-size: 13px; line-height: 1.1; }
  .feature__text { font-size: 10.7px; line-height: 1.3; }
  .feature--audio { top: 290px; }
  .feature--visual { top: 356px; }
  .feature--internet { top: 430px; }

  .contact-band { position: absolute; left: 0; bottom: 0; width: 444px; height: 140px; }
  .contact { position: absolute; left: 32px; top: 556px; }
  .contact__head { font-weight: 700; font-size: 25px; line-height: 1.1; }
  .contact__web { font-size: 15px; font-weight: 400; line-height: 1.3; }
  .contact__web strong { font-weight: 700; }
  .contact__call { font-weight: 700; font-size: 17px; line-height: 1.35; }
  .contact__phone { font-weight: 700; font-size: 17px; color: var(--brand-red); }
  .back-brand {
    position: absolute; right: 26px; top: 580px; width: 86px; font-size: 14px;
  }
  .back-brand .dot {
    display: block; width: 10px; height: 10px; border-radius: 50%;
    background: var(--white); margin: 0 auto 7px;
  }
</style>
</head>
<body>
<main class="canvas">

  <section class="card card--front" aria-label="Postcard front">
    <div class="sea-photo" role="img" aria-label="Aerial photo of a white motor yacht cruising on deep teal sea"></div>
    <h1 class="front-title">
      <span class="thin">FULL</span>
      <span class="bold">YACHT</span>
      <span class="bold bold--wide">SERVICE</span>
    </h1>
    <div class="brand-name front-brand"><span class="dot"></span>Harbor<br>Keep</div>
    <div class="stripe stripe--black"></div>
    <div class="stripe stripe--red"></div>
  </section>

  <section class="card card--back" aria-label="Postcard back">
    <svg class="helm-icon" viewBox="0 0 64 64" fill="none" stroke="#fff" aria-hidden="true">
      <circle cx="32" cy="32" r="21" stroke-width="4"/>
      <circle cx="32" cy="32" r="13" stroke-width="2.5"/>
      <circle cx="32" cy="32" r="4" fill="#fff" stroke="none"/>
      <g stroke-width="3.5" stroke-linecap="round">
        <line x1="32" y1="3" x2="32" y2="19"/>
        <line x1="32" y1="45" x2="32" y2="61"/>
        <line x1="3" y1="32" x2="19" y2="32"/>
        <line x1="45" y1="32" x2="61" y2="32"/>
        <line x1="11.5" y1="11.5" x2="22.8" y2="22.8"/>
        <line x1="41.2" y1="41.2" x2="52.5" y2="52.5"/>
        <line x1="52.5" y1="11.5" x2="41.2" y2="22.8"/>
        <line x1="22.8" y1="41.2" x2="11.5" y2="52.5"/>
      </g>
      <g stroke-width="2.5" stroke-linecap="round">
        <line x1="32" y1="19" x2="32" y2="28"/>
        <line x1="32" y1="36" x2="32" y2="45"/>
        <line x1="19" y1="32" x2="28" y2="32"/>
        <line x1="36" y1="32" x2="45" y2="32"/>
      </g>
    </svg>
    <p class="back-kicker">COMPLETE</p>
    <h2 class="back-title">YATCH SERVICE</h2>
    <div class="title-rule"></div>
    <p class="back-intro">Monthly management plans to ensure the vessel is ready to go at a moments notice. Washing, waxing, detailing, provisioning, crew services and more.</p>

    <div class="feature feature--audio">
      <svg class="feature__icon" viewBox="0 0 34 34" fill="#fff" aria-hidden="true" style="top:2px">
        <path d="M12 6 L30 2 V24 h-3 V8 L15 10.7 V28 h-3 Z"/>
        <ellipse cx="9" cy="28" rx="5" ry="4"/>
        <ellipse cx="25" cy="24" rx="5" ry="4"/>
      </svg>
      <div class="feature__body">
        <div class="feature__name">Audio</div>
        <div class="feature__text">We perform most projects in-house, from<br>design to installation.</div>
      </div>
    </div>

    <div class="feature feature--visual">
      <svg class="feature__icon" viewBox="0 0 34 34" aria-hidden="true" style="top:2px">
        <path d="M1 17 C8 7 26 7 33 17 C26 27 8 27 1 17 Z" fill="#fff"/>
        <circle cx="17" cy="17" r="7" fill="var(--brand-red)"/>
        <circle cx="17" cy="17" r="4" fill="#fff"/>
      </svg>
      <div class="feature__body">
        <div class="feature__name">Visual</div>
        <div class="feature__text">TV's on custom lifts and fold outs.<br>Streaming boxes, media servers and more.</div>
      </div>
    </div>

    <div class="feature feature--internet">
      <svg class="feature__icon" viewBox="0 0 34 34" fill="none" stroke="#fff" stroke-width="3.4" stroke-linecap="round" aria-hidden="true" style="top:-2px">
        <path d="M3 13 C11 5 23 5 31 13"/>
        <path d="M8 18 C13 13 21 13 26 18"/>
        <path d="M13 23 C15 21 19 21 21 23"/>
        <circle cx="17" cy="27" r="1.8" fill="#fff" stroke="none"/>
      </svg>
      <div class="feature__body">
        <div class="feature__name">Internet</div>
        <div class="feature__text">Domestic Connectivity (cellular ) Marina Connecti-<br>vity (Wi-Fi WAN) On board Wi-Fi (2.4GHz &amp; 5Ghz)</div>
      </div>
    </div>

    <svg class="contact-band" viewBox="0 0 444 140" preserveAspectRatio="none" aria-hidden="true">
      <path d="M0 0 L82 10 L444 0 V140 H0 Z" fill="var(--ink-black)"/>
    </svg>
    <div class="contact">
      <div class="contact__head">BOOK ONLINE!</div>
      <div class="contact__web">www.<strong>harborkeep</strong>.us</div>
      <div class="contact__call">or call us:</div>
      <div class="contact__phone">555 -2468 013</div>
    </div>
    <div class="brand-name back-brand"><span class="dot"></span>Harbor<br>Keep</div>
  </section>

</main>
</body>
</html>
```